Bref créative
Stationery design for KORV Holdings
KORV Holdings - Motion Lessons & Media
Use same font as used in my logo
Trajan Bold
Bright & Fun-filled
Damian Whitcombe
IT & Technical Support
The Lumley House
12 Fenwick Lane
Ashcombe-Under-Lyne
Bristol
BS4 7QD
damian@korv.co
www.korv.co
This is the KORV Holdings logo.

```html
<!DOCTYPE html>
<html lang="en">
<head>
<meta charset="utf-8">
<title>KORV Holdings — Business Card</title>
<link rel="stylesheet" href="https://fonts.googleapis.com/css2?family=Cinzel:wght@400;700&family=Lato:wght@400&display=swap">
<style>
  :root {
    --backdrop: #e6e6e6;
    --card-black: #1f1d1e;
    --gold: #d9ad2b;
    --gold-light: #f3d35f;
    --gold-deep: #b8891a;
    --text-gold: #d7ae3f;
  }
  * { margin: 0; padding: 0; box-sizing: border-box; }
  html, body { width: 1200px; height: 987px; overflow: hidden; }
  body {
    background: var(--backdrop);
    position: relative;
    font-family: "Lato", sans-serif;
  }
  .card {
    position: absolute;
    left: 220px;
    width: 760px;
    height: 434px;
    background: var(--card-black);
    border-radius: 26px;
    overflow: hidden;
    box-shadow: 0 14px 30px rgba(0,0,0,0.22);
  }
  .card-back { top: 44px; }
  .card-front { top: 510px; }

  .brand-name {
    font-family: "Cinzel", serif;
    font-weight: 700;
    color: var(--text-gold);
    letter-spacing: 4px;
    line-height: 1;
  }
  .card-back .brand {
    position: absolute;
    left: 0; right: 0; top: 150px;
    text-align: center;
  }
  .card-back .brand-name { font-size: 88px; }
  .card-back .web {
    font-family: "Cinzel", serif;
    color: var(--text-gold);
    font-size: 18px;
    letter-spacing: 6px;
    margin-top: 18px;
  }

  .gold-swoop { position: absolute; left: 0; top: 0; }

  .card-front .brand {
    position: absolute;
    left: 300px; width: 330px; top: 54px;
    text-align: center;
  }
  .card-front .brand-name { font-size: 78px; }
  .card-front .tagline {
    font-family: "Cinzel", serif;
    color: var(--text-gold);
    font-size: 17px;
    letter-spacing: 7px;
    margin-top: 12px;
  }
  .holder {
    position: absolute;
    left: 262px; top: 236px;
    font-family: "Cinzel", serif;
    color: var(--text-gold);
  }
  .holder .name { font-size: 17px; letter-spacing: 1.5px; }
  .holder .role { font-size: 11px; letter-spacing: 1.5px; margin-top: 5px; }

  .contact {
    position: absolute;
    right: 48px; bottom: 36px;
    list-style: none;
    font-family: "Cinzel", serif;
    font-size: 11px;
    color: var(--text-gold);
    letter-spacing: 0.5px;
  }
  .contact li {
    display: flex; align-items: center; gap: 8px;
    line-height: 19px;
  }
  .contact .dot {
    width: 12px; height: 12px; border-radius: 50%;
    background: var(--gold);
    flex: none;
  }
  .contact .indent { padding-left: 20px; }
</style>
</head>
<body>

  <section class="card card-back" aria-label="Card back">
    <div class="brand">
      <div class="brand-name">KORV</div>
      <div class="web">WWW.KORV.CO</div>
    </div>
  </section>

  <section class="card card-front" aria-label="Card front">
    <svg class="gold-swoop" width="760" height="434" viewBox="0 0 760 434" aria-hidden="true">
      <defs>
        <linearGradient id="goldFill" x1="0" y1="0" x2="1" y2="1">
          <stop offset="0" stop-color="var(--gold-light)"/>
          <stop offset="0.55" stop-color="var(--gold)"/>
          <stop offset="1" stop-color="var(--gold-deep)"/>
        </linearGradient>
      </defs>
      <path d="M0 0 H150 C95 110 150 300 262 434 H0 Z" fill="url(#goldFill)"/>
      <path d="M120 0 C70 120 100 300 200 434 L214 434 C120 300 96 140 138 0 Z" fill="var(--card-black)"/>
    </svg>

    <div class="brand">
      <div class="brand-name">KORV</div>
      <div class="tagline">HOLDINGS</div>
    </div>

    <div class="holder">
      <div class="name">DAMIAN WHITCOMBE</div>
      <div class="role">IT &amp; TECHNICAL SUPPORT</div>
    </div>

    <ul class="contact">
      <li><span class="dot"></span>12 Fenwick Lane</li>
      <li class="indent">Ashcombe-Under-Lyne</li>
      <li class="indent">Bristol BS4 7QD</li>
      <li><span class="dot"></span>0117 496 0321</li>
      <li><span class="dot"></span>07700 900 418</li>
      <li><span class="dot"></span>damian@korv.co</li>
      <li><span class="dot"></span>www.korv.co</li>
    </ul>
  </section>

</body>
</html>
```